Stationery Design Project

Require letterhead/stationery design based on new logo (see attached).

Would prefer it kept simple but strong and effective.

Target Market(s)

Clients and building developers. Residential/consumer and corporate clientele.

```html
<!DOCTYPE html>
<html lang="en">
<head>
<meta charset="utf-8">
<title>Keystone Build – DL Window Envelope</title>
<link href="https://fonts.googleapis.com/css2?family=Cinzel:wght@400;700&family=Lato:wght@400;700&display=swap" rel="stylesheet">
<style>
  :root {
    --bg-light: #a9c6cb;
    --bg-mid: #8aa9b0;
    --bg-dark: #5e7f8a;
    --envelope: #202020;
    --brand-grey: #a3a3a3;
    --brand-blue: #3bb4e5;
    --text-grey: #b9b9b9;
    --label-ink: #1c1c1c;
    --window-left: #a7a8ac;
    --window-right: #f0f0f1;
  }
  * { margin: 0; padding: 0; box-sizing: border-box; }
  html, body { width: 1200px; height: 1000px; overflow: hidden; }
  body {
    position: relative;
    background: linear-gradient(200deg, var(--bg-light) 0%, var(--bg-mid) 45%, var(--bg-dark) 100%);
    font-family: "Lato", sans-serif;
  }
  .envelope-dieline { position: absolute; left: 0; top: 0; }
  .brand {
    position: absolute;
    left: 280px;
    top: 232px;
    width: 192px;
    text-align: center;
    color: var(--brand-grey);
    font-family: "Cinzel", serif;
    font-weight: 400;
  }
  .brand-square {
    display: block;
    width: 60px;
    height: 60px;
    margin: 0 auto 36px;
    background: var(--brand-blue);
  }
  .brand-name { display: block; font-size: 34px; line-height: 36px; letter-spacing: 0.5px; }
  .brand-sub { display: block; font-size: 13px; letter-spacing: 9px; line-height: 18px; padding-left: 9px; }
  .return-address {
    position: absolute;
    left: 283px;
    top: 460px;
    font-size: 11px;
    line-height: 15px;
    color: var(--text-grey);
  }
  .return-address .company {
    font-family: "Cinzel", serif;
    font-size: 11.5px;
    letter-spacing: 0.6px;
    color: var(--text-grey);
  }
  .return-address .web { color: var(--brand-blue); font-weight: 700; }
  .format-label {
    position: absolute;
    left: 0;
    width: 1200px;
    top: 900px;
    text-align: center;
    font-family: "Cinzel", serif;
    font-weight: 700;
    font-size: 44px;
    letter-spacing: 1px;
    color: var(--label-ink);
  }
</style>
</head>
<body>
  <svg class="envelope-dieline" width="1200" height="1000" viewBox="0 0 1200 1000" aria-hidden="true">
    <defs>
      <linearGradient id="window-sheen" x1="0" y1="0" x2="1" y2="0">
        <stop offset="0" stop-color="var(--window-left)"/>
        <stop offset="0.35" stop-color="#d8d9db"/>
        <stop offset="1" stop-color="var(--window-right)"/>
      </linearGradient>
    </defs>
    <path fill="var(--envelope)" d="
      M213 132 Q213 108 237 108 L954 108 Q978 108 978 132
      L978 208 L1025 222 L1025 533 L978 547
      L978 873 L213 873
      L213 547 L166 533 L166 222 L213 208 Z"/>
    <rect class="address-window" x="558" y="405" width="351" height="97" rx="14" fill="url(#window-sheen)"/>
  </svg>

  <div class="brand">
    <span class="brand-square"></span>
    <span class="brand-name">KEYSTONE</span>
    <span class="brand-sub">BUILD</span>
  </div>

  <address class="return-address" style="font-style:normal">
    <div class="company">KEYSTONE BUILD.</div>
    <div>Suite 45, Harbour Street, NSW 2000</div>
    <div class="web">www.keystonebuild.com.au</div>
  </address>

  <div class="format-label">DL ENVELOPE (WINDOW)</div>
</body>
</html>
```